I need a bag for flour with windows from the front ill attach some sample title is MAPLE KITCHEN BAKEMIX FLOUR
with color changing on the side stand up pouch I want to be able to put stickers ford different type of flour

Target Market(s)

retail store

Industry/Entity Type

flour retails

Font styles to use
Serif

Colors
0094D4
00A9DD
6FCCEA
C7EBF8
E9F6FB
00AB8E
00BBA5
67D7C9
C6EFE9
E9F9F6

Requirements
Must have
• creative
Nice to have
• I need a place so I can place the stickers of the flour
Should not have
• simple

```html
<!DOCTYPE html>
<html lang="en">
<head>
<meta charset="utf-8">
<title>Maple Kitchen Bakemix Flour – Stand-up Pouch</title>
<link href="https://fonts.googleapis.com/css2?family=Bebas+Neue&family=Cinzel:wght@500&family=Josefin+Sans:wght@300;400&display=swap" rel="stylesheet">
<style>
  :root{
    --stage:#333333;
    --blue-deep:#0094D4;
    --blue:#00A9DD;
    --blue-soft:#6FCCEA;
    --blue-pale:#C7EBF8;
    --blue-mist:#E9F6FB;
    --teal-deep:#00AB8E;
    --teal:#00BBA5;
    --teal-soft:#67D7C9;
    --teal-pale:#C6EFE9;
    --teal-mist:#E9F9F6;
    --title-ink:#0a5f7f;
    --sticker-dark:#55565b;
    --sticker-light:#cdcdd1;
    --sticker-text:#eeeeee;
    --ink:#1f3a44;
  }
  html,body{margin:0;padding:0;}
  body{
    width:1200px;height:1000px;overflow:hidden;
    background:var(--stage);
  }
  .canvas{position:relative;width:1200px;height:1000px;}
  .pouch{position:absolute;left:320px;top:70px;width:560px;height:860px;}
  .pouch svg{display:block;}
  .ribbon-name{font-family:"Cinzel",serif;font-weight:500;fill:var(--teal-mist);}
  .sticker-label{font-family:"Josefin Sans",sans-serif;font-weight:300;fill:var(--sticker-text);letter-spacing:12px;}
  .product-title{font-family:"Bebas Neue",sans-serif;fill:var(--title-ink);}
  .net-weight{font-family:"Josefin Sans",sans-serif;font-weight:400;fill:var(--ink);}
</style>
</head>
<body>
<main class="canvas">
  <div class="pouch">
    <svg width="560" height="860" viewBox="0 0 560 860" xmlns="http://www.w3.org/2000/svg">
      <defs>
        <linearGradient id="sideShift" x1="0" x2="1" y1="0" y2="0">
          <stop offset="0" stop-color="var(--blue-deep)"/>
          <stop offset="0.5" stop-color="var(--blue)"/>
          <stop offset="1" stop-color="var(--teal-deep)"/>
        </linearGradient>
        <linearGradient id="stickerShade" x1="0" x2="1" y1="0" y2="0">
          <stop offset="0" stop-color="var(--sticker-dark)"/>
          <stop offset="1" stop-color="var(--sticker-light)"/>
        </linearGradient>
        <linearGradient id="fieldTone" x1="0" x2="1" y1="0" y2="1">
          <stop offset="0" stop-color="var(--blue-mist)"/>
          <stop offset="0.5" stop-color="var(--teal-pale)"/>
          <stop offset="1" stop-color="var(--blue-soft)"/>
        </linearGradient>
        <linearGradient id="windowTone" x1="0" x2="1" y1="0" y2="1">
          <stop offset="0" stop-color="var(--blue-mist)"/>
          <stop offset="1" stop-color="var(--blue-pale)"/>
        </linearGradient>
        <linearGradient id="ribbonShade" x1="0" x2="1" y1="0" y2="1">
          <stop offset="0" stop-color="var(--teal-deep)"/>
          <stop offset="1" stop-color="var(--teal)"/>
        </linearGradient>
        <clipPath id="pouchShape">
          <path d="M0 30 Q0 0 30 0 H530 Q560 0 560 30 V860 H0 Z"/>
        </clipPath>
      </defs>

      <g clip-path="url(#pouchShape)">
        <rect class="pouch-body" width="560" height="860" fill="url(#sideShift)"/>
        <line class="zip-seal" x1="0" y1="120" x2="560" y2="120" stroke="var(--blue-soft)" stroke-width="3"/>

        <rect class="field-image" x="0" y="515" width="560" height="345" fill="url(#fieldTone)" role="img" aria-label="Soft-focus photo of wheat stalks in light"/>

        <path class="product-window" fill="url(#windowTone)" stroke="var(--blue-pale)" stroke-width="3"
          role="img" aria-label="Clear window showing the flour inside"
          d="M64 288 L92 281 L118 286 L150 278 L190 282 L378 280 L420 276 L468 282 L498 278
             L496 330 L500 380 L494 440 L70 444 L72 400 L66 350 Z"/>

        <path class="sticker-area" fill="url(#stickerShade)"
          d="M78 434 L140 430 L260 433 L380 429 L484 432 L482 505 L486 580 L360 583 L240 580 L120 584 L82 581 L80 510 Z"/>
        <text class="sticker-label" x="287" y="528" font-size="52" text-anchor="middle">STICKER</text>

        <path class="brand-ribbon" fill="url(#ribbonShade)"
          d="M184 0 H378 V305 L367 295 L356 305 L345 295 L334 305 L323 295 L312 305 L301 295 L290 305 L279 295 L268 305 L257 295 L246 305 L235 295 L224 305 L213 295 L202 305 L191 295 L188 305 Z"/>
        <text class="ribbon-name" x="281" y="220" font-size="25" text-anchor="middle">MAPLE</text>
        <line x1="206" y1="232" x2="356" y2="232" stroke="var(--teal-mist)" stroke-width="1"/>
        <text class="ribbon-name" x="281" y="262" font-size="25" text-anchor="middle">KITCHEN</text>

        <circle class="claim-badge" cx="439" cy="248" r="48" fill="var(--blue-deep)"/>

        <line class="title-rule" x1="87" y1="625" x2="475" y2="625" stroke="var(--title-ink)" stroke-width="2"/>
        <text class="product-title" x="87" y="736" font-size="96" textLength="388" lengthAdjust="spacingAndGlyphs">MAPLE KITCHEN</text>
        <line class="title-rule" x1="93" y1="765" x2="469" y2="765" stroke="var(--title-ink)" stroke-width="2"/>

        <text class="net-weight" x="281" y="808" font-size="11" text-anchor="middle">NET. WT. 1 LB. 16 OZ (454 G)</text>
      </g>
    </svg>
  </div>
</main>
</body>
</html>
```